VaultMeridan Business Card Re-Design

VaultMeridan is a specialized information security company that applies its proven methodology of security Assessment, Development, Integration and Training (A-D-I-T) to provide cyber security services in the areas of Data Protection, Network Defense and Compliance. We need the current business card re-designed to properly scale the fonts and possibly rearranging some elements (icons, lettering, etc.) to make the card more appealing to the eye. The card should have the logo that is on the web site (www.vaultmeridan-example.com). We would like ideas for both a black card (black background) and a white card (white background). We prefer rounded corners to help the card stand out but are open to all ideas. FYI: VaultMeridan's slogan is "...your security is our business".

Target Market(s)

#1 US Government Contracting Companies, #2 Commercial Companies, #3 Gen. Public.

Industry/Entity Type

Business

Contact Information for Business Card

See Description; open to the use of different fonts.

Font styles to use
Sans Serif

Colors
000000
ec1f27
ffffff

Requirements
Must have
• Company logo on web site, rounded corners, list of company offerings on the back of the card.
Nice to have
• Icons
Should not have
• none

```html
<!DOCTYPE html>
<html lang="en">
<head>
<meta charset="utf-8">
<title>VaultMeridan Business Cards</title>
<link rel="stylesheet" href="https://fonts.googleapis.com/css2?family=Josefin+Slab:wght@400;600;700&family=Arimo:wght@400&family=Open+Sans:wght@400;600&display=swap">
<style>
  :root {
    --black: #000000;
    --logo-black: #070707;
    --red: #ec1f27;
    --white: #ffffff;
    --stage: #cbcccd;
  }
  * { box-sizing: border-box; margin: 0; padding: 0; }
  html, body { width: 1200px; height: 991px; overflow: hidden; background: var(--stage); }
  .canvas { position: relative; width: 1200px; height: 991px; }

  .card {
    position: absolute;
    width: 598px;
    height: 333px;
    border-radius: 12px;
    overflow: hidden;
  }
  .card svg.swoosh { position: absolute; inset: 0; }

  /* Front */
  .card--front { left: 172px; top: 138px; background: var(--black); }
  .logo-block {
    position: absolute;
    background: var(--logo-black);
    display: flex; flex-direction: column; align-items: center; justify-content: center;
    gap: 8px;
  }
  .card--front .logo-block { left: 28px; top: 26px; width: 160px; height: 196px; }
  .logo-name {
    font-family: "Open Sans", sans-serif; font-weight: 600;
    color: var(--white); font-size: 20px; letter-spacing: 0.5px;
    display: flex; align-items: center; gap: 7px;
  }
  .logo-name .mark { width: 9px; height: 9px; border-radius: 50%; background: var(--red); }
  .logo-tagline { font-family: "Open Sans", sans-serif; color: var(--white); font-size: 9px; }

  .person { position: absolute; left: 245px; top: 38px; font-family: "Josefin Slab", serif; color: var(--red); }
  .person-name { font-size: 28px; font-weight: 600; }
  .person-title { font-size: 17px; font-weight: 600; margin-left: 8px; }
  .person-certs { font-size: 14px; margin-top: -4px; }

  .contact {
    position: absolute; right: 25px; top: 204px; text-align: right;
    font-family: "Josefin Slab", serif; font-weight: 600; color: var(--red); font-size: 14px; line-height: 24px;
  }
  .contact .phone { display: inline-flex; align-items: center; gap: 3px; }
  .contact svg { width: 14px; height: 14px; }
  .contact .emails { font-size: 12px; }
  .address {
    position: absolute; right: 25px; bottom: 20px;
    font-family: "Josefin Slab", serif; font-weight: 600; color: var(--white); font-size: 12.5px;
  }

  /* Back */
  .card--back { left: 430px; top: 520px; background: var(--red); }
  .offerings {
    position: absolute; left: 20px; right: 20px; top: 18px;
    font-family: "Arimo", sans-serif; color: var(--white); font-size: 13px; line-height: 19px; text-align: right;
  }
  .offerings .sep { display: inline-block; width: 7px; height: 7px; border-radius: 50%; background: var(--white); margin: 0 4px 1px; }
  .back-web {
    position: absolute; right: 28px; top: 158px;
    font-family: "Josefin Slab", serif; font-weight: 600; color: var(--white); font-size: 17px;
  }
  .card--back .logo-block { left: 36px; top: 228px; width: 150px; height: 94px; gap: 6px; }
  .card--back .logo-name { font-size: 17px; }
  .card--back .logo-tagline { font-size: 8px; }
</style>
</head>
<body>
<main class="canvas">

  <section class="card card--front" aria-label="Business card front">
    <svg class="swoosh" viewBox="0 0 598 333" aria-hidden="true">
      <path d="M88 333 Q230 160 598 128" fill="none" stroke="var(--red)" stroke-width="4"/>
      <path d="M125 333 Q270 150 598 116" fill="none" stroke="var(--white)" stroke-width="3"/>
      <circle cx="62" cy="313" r="5" fill="var(--white)"/>
    </svg>
    <div class="logo-block">
      <div class="logo-name"><span class="mark"></span>VaultMeridan</div>
      <div class="logo-tagline">Information Security Solutions</div>
    </div>
    <div class="person">
      <div><span class="person-name">Darren Holt</span><span class="person-title">- President CEO</span></div>
      <div class="person-certs">CISSP , CIEH</div>
    </div>
    <div class="contact">
      <div>
        <span class="phone"><svg viewBox="0 0 16 16"><circle cx="8" cy="8" r="8" fill="var(--red)"/><path d="M5 4.2c.5-.4 1-.3 1.3.2l.7 1.2c.2.4.1.8-.2 1l-.5.4c.4.9 1.2 1.8 2.2 2.3l.4-.5c.3-.3.7-.4 1-.2l1.2.7c.5.3.5.9.1 1.3-.9 1-2.2.9-3.4.1C6.1 9.7 5 8.4 4.4 7c-.4-1.1-.3-2.1.6-2.8z" fill="var(--black)"/></svg>555.014.2201</span>
        <span class="phone"><svg viewBox="0 0 16 16"><rect x="3.5" y="0.5" width="9" height="15" rx="2" fill="var(--red)"/><rect x="5.5" y="2.5" width="5" height="9" fill="var(--black)"/></svg>555.018.3627</span>
      </div>
      <div>www.vaultmeridan-example.com</div>
      <div class="emails">info@vaultmeridan-example.com, dholt@vaultmeridan-example.com</div>
    </div>
    <div class="address">VaultMeridan, Inc. 4120 Harbor Ln. Suite 210 Easton Maryland 21601</div>
  </section>

  <section class="card card--back" aria-label="Business card back">
    <svg class="swoosh" viewBox="0 0 598 333" aria-hidden="true">
      <path d="M0 212 Q300 132 598 330 L598 333 L0 333 Z" fill="var(--black)"/>
      <path d="M0 192 Q300 112 598 312" fill="none" stroke="var(--white)" stroke-width="4"/>
      <path d="M0 202 Q300 122 598 321" fill="none" stroke="var(--black)" stroke-width="3"/>
      <path d="M0 207 Q300 127 598 326" fill="none" stroke="var(--red)" stroke-width="3"/>
    </svg>
    <div class="offerings">
      <p>Secure Cloud &amp; Open Stack Solutions<span class="sep"></span>Network Attack Penetration &amp; Defense</p>
      <p>Red/Blue Team<span class="sep"></span>Data Center Consolidation<span class="sep"></span>Secure Virtual Computing</p>
      <p>Classified Cross Domain Solutions<span class="sep"></span>Foreign/Counter Intelligence Data Security</p>
      <p>Certification &amp; Accreditation<span class="sep"></span>Secure Wireless Solutions<span class="sep"></span>Security<span class="sep"></span>Training</p>
      <p>Assessment &amp; integration<span class="sep"></span>Security Subject Matter Experts</p>
      <p>Executive Security Strategy Coaching</p>
      <p>Data Encryption/Privacy</p>
    </div>
    <div class="back-web">www.vaultmeridan-example.com</div>
    <div class="logo-block">
      <div class="logo-name"><span class="mark"></span>VaultMeridan</div>
      <div class="logo-tagline">Information Security Solutions</div>
    </div>
  </section>

</main>
</body>
</html>
```